High-end construction company needs a business card design

We need a modern looking business card that draws people in, is memorable and looks so good people will want to sick it on their fridges.
On the first side what is needed are:
Logo
My name - Tomas Verbelk
Title - Managing Director
Website - www.kravel.co.uk
Email - tomas@kravel.co.uk
Telephone - 020 5194 6381
Mobile - 07845319027
On the back side was is needed is a list of all the services we provide:
-Kitchen Renovations
-Bathroom Renovations
-House Renovations
-Garage Conversions
-Extensions
-Loft Conversions
-Conservatories
-Carpentry
-Tiling
-Electrical
-Plumbing & Heating
-Bricklaying
-Landscaping
-Decorating
-Plastering
We would like the colours to be the same shades as on the logo with grey or black for the words.
Target Market(s)
Anyone who needs building work done
Contact Information for Business Card
This business card is for a construction company which strives to deliver excellent service and quality.
The look and feel of the card should represent this.
Requirements
Must have
- On the first side what is needed are:
Logo
My name - Tomas Verbelk
Title - Managing Director
Website - www.kravel.co.uk
Email - tomas@kravel.co.uk
Telephone - 020 5194 6381
Mobile - 07845319027
Nice to have
- Cool looking features

```html
<!DOCTYPE html>
<html lang="en">
<head>
<meta charset="utf-8">
<title>Kravel Construction Ltd – Business Card</title>
<link rel="stylesheet" href="https://fonts.googleapis.com/css2?family=Ubuntu:wght@500;700&display=swap">
<style>
  :root {
    --mint: #cde8d8;
    --white: #ffffff;
    --charcoal: #353334;
    --ink: #333333;
    --grey: #9a9a9a;
    --green-light: #76bd43;
    --green-dark: #4a8f3a;
  }
  * { box-sizing: border-box; margin: 0; padding: 0; }
  html, body { width: 1169px; height: 1200px; overflow: hidden; }
  body {
    position: relative;
    background: var(--mint);
    font-family: "Ubuntu", sans-serif;
  }
  .card {
    position: absolute;
    left: 154px;
    width: 861px;
    height: 492px;
    background: var(--white);
    overflow: hidden;
  }
  .card--front { top: 93px; }
  .card--back { top: 615px; }

  .brand {
    position: absolute;
    text-align: center;
    color: var(--green-light);
    font-weight: 700;
    line-height: 1;
  }
  .brand__name { font-size: 58px; letter-spacing: 2px; display: block; }
  .brand__sub { font-size: 15.5px; letter-spacing: 3.2px; display: block; margin-top: 8px; }
  .card--front .brand { left: 90px; top: 250px; width: 270px; }
  .card--back .brand { left: 296px; top: 108px; width: 270px; }

  .holder { position: absolute; left: 431px; top: 110px; }
  .holder__name { font-size: 41px; font-weight: 700; color: var(--ink); line-height: 1.1; }
  .holder__name span { color: var(--grey); font-weight: 500; }
  .holder__title { font-size: 26px; font-weight: 500; color: var(--green-dark); line-height: 1.1; margin-top: 1px; }

  .contacts { position: absolute; left: 431px; top: 217px; list-style: none; }
  .contacts li {
    display: flex; align-items: center;
    height: 31px; margin-bottom: 14px;
    font-size: 29px; font-weight: 500; color: var(--grey);
  }
  .contacts li:nth-child(2) { margin-bottom: 12px; }
  .contacts li:nth-child(3) { margin-bottom: 18px; }
  .contacts svg { width: 31px; height: 31px; margin-right: 31px; flex: none; }

  .stripe { position: absolute; left: 0; width: 861px; }
  .stripe--accent { top: 430px; height: 16px; }
  .stripe--base { top: 446px; height: 46px; background: var(--charcoal); }

  .back-band { position: absolute; left: 0; top: 0; width: 861px; height: 246px; background: var(--charcoal); }
  .services__heading {
    position: absolute; left: 31px; top: 270px;
    font-size: 38px; font-weight: 700; color: var(--green-dark);
  }
  .services__col { position: absolute; top: 335px; list-style: none; }
  .services__col li {
    font-size: 25px; font-weight: 500; color: var(--grey);
    line-height: 27px; white-space: nowrap;
  }
  .services__col li::before { content: "•"; color: var(--green-light); margin-right: 5px; }
  .services__col--a { left: 31px; }
  .services__col--b { left: 330px; }
  .services__col--c { left: 592px; }
</style>
</head>
<body>

<section class="card card--front">
  <div class="brand">
    <span class="brand__name">KRAVEL</span>
    <span class="brand__sub">CONSTRUCTION LTD</span>
  </div>

  <div class="holder">
    <h1 class="holder__name">Tomas <span>Verbelk</span></h1>
    <p class="holder__title">Managing Director</p>
  </div>

  <ul class="contacts">
    <li>
      <svg viewBox="0 0 31 31" aria-hidden="true"><rect width="31" height="31" rx="5" fill="#76bd43"/><path d="M9 7c2 0 3 4 3 5s-2 1-2 2c0 2 4 6 6 6 1 0 1-2 2-2s5 1 5 3-2 3-4 3C12 24 7 19 7 10c0-2 1-3 2-3z" fill="#fff"/></svg>
      020 5194 6381
    </li>
    <li>
      <svg viewBox="0 0 31 31" aria-hidden="true"><rect width="31" height="31" rx="5" fill="#76bd43"/><rect x="10" y="5" width="11" height="21" rx="2" fill="none" stroke="#fff" stroke-width="2"/><circle cx="15.5" cy="22.5" r="1.2" fill="#fff"/></svg>
      07845319027
    </li>
    <li>
      <svg viewBox="0 0 31 31" aria-hidden="true"><rect width="31" height="31" rx="5" fill="#76bd43"/><rect x="6" y="9" width="19" height="13" fill="none" stroke="#fff" stroke-width="1.8"/><path d="M6 9l9.5 8L25 9M6 22l7-6M25 22l-7-6" fill="none" stroke="#fff" stroke-width="1.5"/></svg>
      tomas@kravel.co.uk
    </li>
    <li>
      <svg viewBox="0 0 31 31" aria-hidden="true"><rect width="31" height="31" rx="5" fill="#76bd43"/><g fill="none" stroke="#fff" stroke-width="1.5"><circle cx="15.5" cy="15.5" r="9"/><ellipse cx="15.5" cy="15.5" rx="4" ry="9"/><path d="M6.5 15.5h18M8 11h15M8 20h15"/></g></svg>
      www.kravel.co.uk
    </li>
  </ul>

  <svg class="stripe stripe--accent" viewBox="0 0 861 16" preserveAspectRatio="none" aria-hidden="true">
    <rect width="861" height="16" fill="#76bd43"/>
    <polygon points="0,0 400,0 394,16 0,16" fill="#4a8f3a"/>
  </svg>
  <div class="stripe stripe--base"></div>
</section>

<section class="card card--back">
  <div class="back-band"></div>
  <div class="brand">
    <span class="brand__name">KRAVEL</span>
    <span class="brand__sub">CONSTRUCTION LTD</span>
  </div>

  <h2 class="services__heading">Services:</h2>
  <ul class="services__col services__col--a">
    <li>Kitchen Renovations</li>
    <li>Bathroom Renovations</li>
    <li>House Renovations</li>
    <li>Garage Conversions</li>
    <li>Extensions</li>
  </ul>
  <ul class="services__col services__col--b">
    <li>Loft Conversions</li>
    <li>Conservatories</li>
    <li>Carpentry</li>
    <li>Tiling</li>
    <li>Electrical</li>
  </ul>
  <ul class="services__col services__col--c">
    <li>Plumbing &amp; Heating</li>
    <li>Bricklaying</li>
    <li>Landscaping</li>
    <li>Decorating</li>
    <li>Plastering</li>
  </ul>
</section>

</body>
</html>
```